Two Day Training Event includes a Dinner/Bowling Party at Pinhollow in Troy, MI

I would like a postcard to attract Insurance Agents to an KRV meeting calling it a summit or something like that. Just something to mail to insurance agents telling them about our upcoming event with over 20 carriers. An opportunity to certify face to face with MAPD carriers and see what 2020 has to offer. Prior to OEP OPen Enrollment and AEP Annual Election period we have a number of meetings. Carriers want to come especially if we can get a number of agents. We are going to go to Pinhollow a fun bowling alley for dinner, drinks and bowling to network and talk about the upcoming year.

Target Market(s)

Existing and new insurance agents

Industry/Entity Type

Insurance Broker

Contact Information for Business Card

Looking for a new card design I sent my LOGO and can upload my existing card.

Font styles to use
Serif

Colors

Designer to choose colors to be used in the design.

Requirements
Must have
• Dates Sept 16 and 17th
• location Larkfield Conference Hall in Troy MI
• times
Nice to have
• It would be nice to see a fun design.

```html
<!DOCTYPE html>
<html lang="en">
<head>
<meta charset="utf-8">
<title>KRV Alliance Two Day Training Event Postcard</title>
<link href="https://fonts.googleapis.com/css2?family=Montserrat:ital,wght@0,400;0,500;0,700;0,800;0,900;1,400;1,500;1,700;1,800;1,900&display=swap" rel="stylesheet">
<style>
  :root {
    --navy: #0d1645;
    --navy-mid: #1b2c62;
    --ink-blue: #262c6e;
    --brand-blue: #3240a0;
    --yellow: #f7e91b;
    --gold: #d6a23e;
    --gold-dark: #b07a26;
    --paper: #ffffff;
    --text: #24262e;
    --stage: #eceef1;
  }
  * { box-sizing: border-box; margin: 0; padding: 0; }
  html, body { width: 1200px; height: 1110px; overflow: hidden; background: var(--stage); }
  body { font-family: "Montserrat", Arial, sans-serif; position: relative; }

  .postcard {
    position: absolute; left: 240px; width: 720px; height: 518px;
    background: var(--paper); overflow: hidden;
    box-shadow: 0 4px 14px rgba(0,0,0,.18);
  }
  .postcard--front { top: 25px; }
  .postcard--back { top: 567px; }

  .wave { position: absolute; inset: 0; width: 720px; height: 518px; }

  /* front */
  .event-photo {
    position: absolute; right: 0; top: 0; width: 430px; height: 340px;
    background:
      linear-gradient(90deg, #fff 0%, rgba(255,255,255,.55) 30%, rgba(255,255,255,0) 60%),
      linear-gradient(180deg, rgba(255,255,255,0) 60%, #fff 100%),
      radial-gradient(ellipse at 60% 25%, #f4d9a8 0%, #c9a67a 30%, #6b6258 65%, #3c3c44 100%);
  }
  .brand {
    position: absolute; left: 38px; top: 78px;
    font-weight: 800; font-size: 48px; line-height: 1; color: var(--brand-blue);
  }

  .headline { position: absolute; left: 0; top: 172px; font-style: italic; font-weight: 900; line-height: 1; }
  .headline__band {
    background: var(--ink-blue); color: var(--yellow);
    width: 347px; height: 60px; padding-left: 36px; font-size: 56px;
    display: flex; align-items: center;
    clip-path: polygon(0 0, 100% 0, 95% 100%, 0 100%);
  }
  .headline__line { color: var(--ink-blue); padding-left: 34px; }
  .headline__line--training { font-size: 55px; margin-top: 2px; }
  .headline__line--event { font-size: 80px; padding-left: 32px; }

  .date-block { position: absolute; right: 30px; top: 376px; text-align: right; color: #fff; font-style: italic; line-height: 1.12; }
  .date-block__month { font-size: 29px; font-weight: 500; }
  .date-block__days { font-size: 35px; font-weight: 500; color: var(--yellow); }
  .date-block__time { font-size: 33px; font-weight: 500; }
  .date-block__time span { color: var(--yellow); }

  .venue { position: absolute; left: 32px; top: 472px; color: #fff; font-style: italic; font-weight: 500; font-size: 18px; white-space: nowrap; }

  /* back */
  .pitch {
    position: absolute; left: 32px; top: 46px; width: 328px;
    font-style: italic; font-size: 18px; letter-spacing: -0.2px; line-height: 1.38;
    color: var(--text); text-align: justify;
  }
  .stamp-box { position: absolute; left: 588px; top: 16px; width: 114px; height: 115px; border: 2px solid var(--brand-blue); }
  .address-line { position: absolute; left: 409px; width: 255px; height: 0; border-top: 1.5px solid #222; }
  .rsvp { position: absolute; left: 33px; top: 361px; color: #fff; font-style: italic; font-size: 13px; line-height: 1.32; }
  .rsvp strong { font-weight: 700; }
  .rsvp .phone { color: var(--yellow); font-weight: 700; }
  .venue--back { left: 32px; top: 472px; }
</style>
</head>
<body>

<section class="postcard postcard--front">
  <div class="event-photo" role="img" aria-label="Photo of a conference audience seated facing a speaker at a lit stage"></div>

  <svg class="wave" viewBox="0 0 720 518" aria-hidden="true">
    <defs>
      <linearGradient id="goldFront" x1="0" x2="1">
        <stop offset="0" stop-color="#b07a26"/>
        <stop offset=".5" stop-color="#d6a23e"/>
        <stop offset="1" stop-color="#f3d27a"/>
      </linearGradient>
    </defs>
    <path d="M0,378 C70,425 200,440 320,428 C240,446 110,446 0,432 Z" fill="url(#goldFront)"/>
    <path d="M0,438 C170,448 340,432 470,340 C560,280 640,258 720,255 L720,518 L0,518 Z" fill="#1b2c62"/>
    <path d="M0,444 L720,430 L720,518 L0,518 Z" fill="#0d1645"/>
  </svg>

  <div class="brand">KRV Alliance</div>

  <h1 class="headline">
    <div class="headline__band">TWO DAY</div>
    <div class="headline__line headline__line--training">TRAINING</div>
    <div class="headline__line headline__line--event">EVENT</div>
  </h1>

  <div class="date-block">
    <div class="date-block__month">September</div>
    <div class="date-block__days">16th &amp; 17th</div>
    <div class="date-block__time">at <span>7:00PM</span></div>
  </div>

  <p class="venue">Larkfield Conference Hall, Troy MI</p>
</section>

<section class="postcard postcard--back">
  <svg class="wave" viewBox="0 0 720 518" aria-hidden="true">
    <defs>
      <linearGradient id="goldBack" x1="0" x2="1">
        <stop offset="0" stop-color="#b07a26"/>
        <stop offset=".5" stop-color="#d6a23e"/>
        <stop offset="1" stop-color="#f3d27a"/>
      </linearGradient>
    </defs>
    <path d="M420,438 C540,440 660,420 720,380 L720,428 C640,446 520,448 420,438 Z" fill="url(#goldBack)"/>
    <path d="M0,252 C90,242 170,270 260,330 C370,405 520,440 720,436 L720,518 L0,518 Z" fill="#1b2c62"/>
    <path d="M0,330 C120,350 200,380 300,410 C420,440 560,446 720,436 L720,518 L0,518 Z" fill="#0d1645"/>
  </svg>

  <p class="pitch">We will have over 20 carriers with an opportunity to see what is offered for 2020 OEP Individual Health Insurance and AEP for MAPD and PDP carriers. Plus we can certify for all MAPD carriers who require face to face certifications.</p>

  <div class="stamp-box"></div>
  <div class="address-line" style="top:204px"></div>
  <div class="address-line" style="top:265px"></div>
  <div class="address-line" style="top:327px"></div>

  <p class="rsvp">
    <strong>Please RSVP</strong><br>
    no later than<br>
    <strong>August 29, 2019</strong><br>
    to Marla at <strong>marla@krvalliance.com</strong> or<br>
    call <span class="phone">248-555-0147</span>
  </p>

  <p class="venue venue--back">Larkfield Conference Hall, Troy MI</p>
</section>

</body>
</html>
```